Zielgruppe
Ich bin Fotograf und habe mich auf Schwangerschafts- und Neugeborenenfotografie spezialisiert. Meine Zielgruppe sind schwangere Frauen im letzten Drittel der Schwangerschaft und frisch gewordene Eltern.
Aufgabenstellung
- sehr schlichtes Design, in der Anlage finden Sie zwei der meist verkauften Karten damit Sie sich vom Stil eine Vorstellung machen können
- Lieferung als offene Indesign 5.5 Datei (so das die Farben, Texte, .... angepasst werden können)
- 2-3 Bilder (querformat) sollen in das Design eingearbeitet werden können
- Die Karten werden von mir nachher als fertig gedruckte Karte an meine Kunden verkauft, dies bitte ich zu berücksichtigen
- ich möchte die Karten so nutzen können das sowohl Geburtskarten für Jungs wie auch für Mädels erstellt werden können
- Format: Din A6 (geschlossen 105x148mm), Klappkarte, hoch, 3mm Beschnitt

```html
<!DOCTYPE html>
<html lang="de">
<head>
<meta charset="utf-8">
<title>Geburtskarte Liana</title>
<link rel="stylesheet" href="https://fonts.googleapis.com/css2?family=Raleway:wght@500;700&family=Pinyon+Script&display=swap">
<style>
  :root {
    --paper: #ffffff;
    --blush: #f8c1aa;
    --slate: #6c6d6f;
    --text-light: #ffffff;
    --photo-light: #f4f1ef;
    --photo-skin: #e9cdbf;
    --photo-sepia-light: #f3efea;
    --photo-sepia: #d9cfc6;
  }
  * { margin: 0; padding: 0; box-sizing: border-box; }
  html, body {
    width: 1200px;
    height: 442px;
    overflow: hidden;
    background: var(--paper);
  }
  .card {
    position: relative;
    width: 1200px;
    height: 442px;
    background: var(--paper);
  }
  .tile { position: absolute; }
  .tile--blank { left: 0; top: 0; width: 598px; height: 220px; background: var(--paper); }
  .tile--blush-top { left: 598px; top: 0; width: 292px; height: 220px; background: var(--blush); }
  .tile--photo-top {
    left: 890px; top: 0; width: 308px; height: 220px;
    background: linear-gradient(180deg, var(--photo-light) 0%, var(--photo-skin) 55%, var(--photo-light) 100%);
  }
  .tile--message {
    left: 2px; top: 221px; width: 600px; height: 219px;
    background: var(--slate);
    color: var(--text-light);
    font-family: "Raleway", Arial, sans-serif;
    padding: 73px 40px 0 54px;
  }
  .tile--photo-bottom {
    left: 602px; top: 221px; width: 288px; height: 221px;
    background: radial-gradient(ellipse at 55% 55%, var(--photo-sepia) 0%, var(--photo-sepia-light) 75%);
  }
  .tile--name {
    left: 890px; top: 221px; width: 308px; height: 221px;
    background: var(--blush);
    display: flex; align-items: center; justify-content: center;
  }
  .message__lead {
    font-weight: 700;
    font-size: 13px;
    line-height: 18px;
    margin-bottom: 13px;
  }
  .message__body {
    font-weight: 700;
    font-size: 12.5px;
    line-height: 19px;
    max-width: 520px;
  }
  .baby-name {
    font-family: "Pinyon Script", "Great Vibes", cursive;
    font-weight: 400;
    font-size: 74px;
    color: var(--text-light);
    line-height: 1;
    margin-top: 6px;
  }
</style>
</head>
<body>
  <main class="card">
    <div class="tile tile--blank"></div>
    <div class="tile tile--blush-top"></div>
    <div class="tile tile--photo-top" role="img" aria-label="Foto: Neugeborenes mit kleinen Flügeln auf weißer Decke liegend"></div>

    <section class="tile tile--message">
      <p class="message__lead">Lorem ipsum dolor sit amet,<br>Aenean commodo ligula eget dolor</p>
      <p class="message__body">Lorem ipsum dolor sit amet, consectetuer adipiscing elit. Aenean commodo ligula eget dolor. Aenean massa. Cum sociis natoque penatibus et magnis dis parturient montes, na</p>
    </section>

    <div class="tile tile--photo-bottom" role="img" aria-label="Foto in Sepia: schlafendes Neugeborenes mit Engelsflügeln auf flauschiger Decke"></div>

    <div class="tile tile--name">
      <h1 class="baby-name">Liana</h1>
    </div>
  </main>
</body>
</html>
```